Need a book cover design for a Lumora Book

Book has a long title and sub title so lots of words to fit on the cover.

I can be flexible a bit with the sub title due to the length of it but ideally i can get a design that takes everything.

Here is the title:

Tidal Geology: The Roots of Erosion, Sedimentation, and Canyon Forming

Sub Title/Heading
An Easy Primer on Coastal Cliffs, Dune Drift, River Beds, and Delta Mapping Methods

```html
<!DOCTYPE html>
<html lang="en">
<head>
<meta charset="utf-8">
<title>Tidal Geology — Book Cover</title>
<link rel="stylesheet" href="https://fonts.googleapis.com/css2?family=Bebas+Neue&family=League+Gothic&family=Montserrat:wght@300;600&display=swap">
<style>
  :root {
    --stage: #000000;
    --cover-pink: #ff3f9c;
    --mint: #c6fcd3;
    --emblem-deep: #c6409e;
    --ink-white: #ffffff;
    --next-pink: #ff4aa0;
    --next-green: #a3d4a0;
  }
  * { margin: 0; padding: 0; box-sizing: border-box; }
  html, body {
    width: 1200px; height: 1200px; overflow: hidden;
    background: var(--stage);
  }
  .stage { position: relative; width: 1200px; height: 1200px; }

  .cover {
    position: absolute; left: 238px; top: 61px;
    width: 720px; height: 1080px;
    background: var(--cover-pink);
    overflow: hidden;
    color: var(--mint);
  }

  .title-line {
    position: absolute; left: 60px;
    font-family: "Bebas Neue", "Oswald", sans-serif;
    font-size: 222px; line-height: 0.8;
    letter-spacing: 2px;
    white-space: nowrap;
  }
  .title-line--one { top: 105px; }
  .title-line--two { top: 283px; }
  .stem { position: relative; display: inline-block; }
  .stem::before {
    content: ""; position: absolute;
    left: 50%; transform: translateX(-50%);
    bottom: 70%; width: 21px; height: 420px;
    background: var(--mint);
  }

  .spine-rule {
    position: absolute; left: 424px; top: 452px;
    width: 24px; height: 640px;
    background: var(--mint);
  }

  .subheading {
    position: absolute; left: 60px; top: 452px;
    width: 345px;
    font-family: "League Gothic", "Bebas Neue", sans-serif;
    font-size: 62px; line-height: 56px;
    text-transform: uppercase; letter-spacing: 0.5px;
    white-space: nowrap;
  }

  .divider {
    position: absolute; left: 60px; top: 762px;
    width: 116px; height: 2px;
    background: var(--mint);
  }

  .tagline {
    position: absolute; left: 60px; top: 786px;
    font-family: "Montserrat", sans-serif;
    font-size: 21px; line-height: 27px;
    color: var(--ink-white); font-weight: 300;
  }
  .tagline strong { font-weight: 600; }

  .author {
    position: absolute; left: 60px; top: 984px;
    font-family: "Montserrat", sans-serif;
    font-size: 25px; font-weight: 300; letter-spacing: 1px;
    color: var(--ink-white);
    -webkit-text-stroke: 0.4px #1a1a1a;
  }

  .emblem {
    position: absolute; left: 500px; top: 740px;
    width: 180px; height: 180px; border-radius: 50%;
    background: radial-gradient(circle at 50% 50%, var(--emblem-deep) 0 22%, var(--mint) 23% 100%);
    opacity: 0.9;
  }

  .next-cover {
    position: absolute; left: 1165px; top: 86px;
    width: 35px; height: 1024px;
    background: var(--next-pink);
  }
  .next-cover__band {
    position: absolute; left: 0; bottom: 0;
    width: 100%; height: 78px;
    background: var(--next-green);
  }
</style>
</head>
<body>
<main class="stage">
  <section class="cover" aria-label="Book cover: Tidal Geology">
    <h1 class="book-title">
      <span class="title-line title-line--one">T<span class="stem">I</span>DAL</span>
      <span class="title-line title-line--two">GEOLOGY</span>
    </h1>
    <div class="spine-rule"></div>

    <h2 class="subheading">The Roots of<br>Erosion,<br>Sedimentation,<br>and Canyon<br>Forming</h2>

    <div class="divider"></div>

    <p class="tagline">An Easy Primer on<br><strong>Coastal Cliffs, Dune Drift,</strong><br><strong>River Beds,</strong> and <strong>Delta</strong><br><strong>Mapping Methods</strong></p>

    <p class="author">AUTHOR NAME</p>

    <div class="emblem" role="img" aria-label="Round emblem of layered rock strata meeting ocean waves"></div>
  </section>

  <div class="next-cover"><div class="next-cover__band"></div></div>
</main>
</body>
</html>
```